SkyVelour IOS App for iPhone / Luxury private aviation / 1 main screen

Hello there !

SkyVelour Ltd is a VIP aircraft operator. You can see our https://facebook.example/skyvelour page or our https://instagram.example/sky_velour . Our web page http://skyvelour.example says it all, we don't communicate much except for the music industry activities we have.

We have developed a very simple app, 6 screens total, that will give the user a distance and a flight time between any two airports of the world. Enter a departure point (New York or JFK or KJFK...) and a destination (like Los Angeles, LAX or KLAX) and we will give you the flight time depending on the type of private jet you are selecting in the aircraft database of the app.

You might want to see the attached pdf for the flow...Any design idea is welcome.

We want it to be simple, pure, fast, and of course less will be more. We should see a unity between all these screens, same design spirit of course... On the main screen of the app, we are showing:- the company logo- a departure airport- a destination airport- the selected aircraft with access to a mini photo gallery of the said airplane- a flight time shown in hours and minutes- a distance shown in Miles, Nautical Miles or KM according to the pref page selection- an access to a contact screen- an access to a parameters screen (will develop some of it on a later version).

Thanks !!

Mathis

Target Market(s)

Private aircraft travelers and VIP flights brokers

Industry/Entity Type

Aviation

Font styles to use
Sans Serif

Colors
aaaaaa
5c5c5c
1b1b1b
e9e9e9
ffffff

Requirements
Must have
• Our logo
Nice to have
• Elegant design
Should not have
• Complicated stuff

```html
<!DOCTYPE html>
<html lang="en">
<head>
<meta charset="utf-8">
<title>SkyVelour – App Screens</title>
<link href="https://fonts.googleapis.com/css2?family=Jost:wght@400;500;600&display=swap" rel="stylesheet">
<style>
  :root{
    --blue:#0b0bef;
    --ink:#1b1b1b;
    --mid:#5c5c5c;
    --soft:#aaaaaa;
    --line:#e9e9e9;
    --paper:#ffffff;
    --screen:#fafafa;
    --map:#dcdcfb;
  }
  *{box-sizing:border-box;margin:0;padding:0}
  html,body{width:1200px;height:2203px;overflow:hidden;background:var(--paper);font-family:"Jost",sans-serif;color:var(--ink)}
  .board{position:relative;width:1200px;height:2203px}
  .screen{position:absolute;width:233px;height:509px;background:var(--screen);border-radius:20px;overflow:hidden;box-shadow:0 10px 30px rgba(0,0,0,.08),0 0 0 1px var(--line)}
  .screen > *{position:absolute}
  .caption{position:absolute;width:233px;text-align:center;font-size:22px;font-weight:500;letter-spacing:1.5px;color:var(--ink)}
  .clock{top:10px;left:22px;font-size:8px;font-weight:500}
  .header{top:30px;left:0;width:100%;text-align:center;font-size:11px;color:var(--ink)}
  .back{top:31px;left:12px;width:12px;height:10px}
  .wordmark{width:100%;left:0;text-align:center;letter-spacing:.35em;color:var(--mid);font-weight:400}
  .heading{font-size:11px;font-weight:600;color:var(--ink)}
  .card{background:var(--paper);border-radius:6px;box-shadow:0 2px 10px rgba(0,0,0,.06)}
  .label{font-size:7px;color:var(--mid)}
  .value{font-size:10px;color:var(--ink)}
  .photo{border-radius:4px}
  .round-btn{width:26px;height:26px;border-radius:50%;background:var(--blue);display:flex;align-items:center;justify-content:center}
  .pill{background:var(--blue);color:var(--paper);border-radius:14px;font-size:8px;font-weight:500;letter-spacing:.08em;display:flex;align-items:center;justify-content:center}
  .row{left:8px;right:8px;display:flex;justify-content:space-between;font-size:9px;color:var(--mid)}
  .row b{font-weight:400;color:var(--ink)}
  .faded{opacity:.07}
  .sheet{background:var(--paper);box-shadow:0 -4px 14px rgba(0,0,0,.08)}
  .app{width:60px;text-align:center;font-size:6px;color:var(--mid)}
  .app i{display:block;width:14px;height:14px;border-radius:50%;margin:0 auto 4px;border:2px solid}
  .contact-title{left:10px;font-size:11px;font-weight:600}
  .contact-text{left:10px;font-size:10px;color:var(--mid)}
  .social{width:32px;height:32px;border-radius:50%}
</style>
</head>
<body>
<div class="board">

  <!-- Splash -->
  <section class="screen" style="left:94px;top:98px">
    <span class="clock">9:41</span>
    <div class="wordmark" style="top:272px;font-size:24px;letter-spacing:.3em">SKYVELOUR</div>
  </section>
  <div class="caption" style="left:94px;top:640px">Splash Screen</div>

  <!-- Home -->
  <section class="screen" style="left:483px;top:98px">
    <span class="clock">9:41</span>
    <div class="wordmark" style="top:50px;font-size:8px">SKYVELOUR</div>
    <div class="heading" style="top:86px;left:10px">Choose Airports</div>
    <div class="card" style="top:112px;left:10px;width:213px;height:102px">
      <svg style="position:absolute;left:8px;top:20px" width="8" height="64" viewBox="0 0 8 64"><circle cx="4" cy="3" r="2.5" fill="none" stroke="#0b0bef" stroke-width="1.2"/><line x1="4" y1="7" x2="4" y2="57" stroke="#0b0bef" stroke-width="1" stroke-dasharray="3 2"/><circle cx="4" cy="60" r="2.5" fill="#0b0bef"/></svg>
      <div class="label" style="position:absolute;left:20px;top:22px">Departure</div>
      <div class="value" style="position:absolute;left:20px;top:34px">New York - JFK</div>
      <div style="position:absolute;left:20px;right:14px;top:50px;height:1px;background:var(--line)"></div>
      <div class="label" style="position:absolute;left:20px;top:57px">Arrival</div>
      <div class="value" style="position:absolute;left:20px;top:69px">Sydney - SYD</div>
      <div class="round-btn" style="position:absolute;left:182px;top:41px;width:20px;height:20px">
        <svg width="10" height="10" viewBox="0 0 10 10"><path d="M3.5 8.5V1.5M1.8 3.2 3.5 1.5 5.2 3.2M6.5 1.5v7M4.8 6.8 6.5 8.5 8.2 6.8" fill="none" stroke="#fff" stroke-width="1"/></svg>
      </div>
    </div>
    <div class="heading" style="top:234px;left:10px">Choose a Jet</div>
    <div style="top:238px;right:10px;font-size:6px;color:var(--blue)">View All</div>
    <div class="photo" style="top:262px;left:-4px;width:6px;height:96px;background:linear-gradient(#5a5f7a,#2b2e3e)"></div>
    <div class="photo" role="img" aria-label="Private jet parked on the apron at dusk" style="top:259px;left:10px;width:213px;height:103px;background:linear-gradient(180deg,#3a4a8a 0%,#8a8db8 45%,#c9b8c0 58%,#2c2f3d 75%,#15161d 100%)"></div>
    <div class="photo" style="top:262px;left:231px;width:6px;height:96px;background:linear-gradient(#e9a86a,#6a4a3a)"></div>
    <div class="value" style="top:370px;left:10px;line-height:15px">Meridian Grand Express<br>XR</div>
    <div class="round-btn" style="top:466px;left:10px">
      <svg width="12" height="12" viewBox="0 0 12 12"><circle cx="6" cy="6" r="3.6" fill="none" stroke="#fff" stroke-width="2.2" stroke-dasharray="1.6 1.2"/><circle cx="6" cy="6" r="1.4" fill="#fff"/></svg>
    </div>
    <div class="pill" style="top:465px;left:123px;width:100px;height:28px">VIEW DETAILS</div>
  </section>
  <div class="caption" style="left:483px;top:640px">Home Screen</div>

  <!-- Gallery -->
  <section class="screen" style="left:872px;top:98px">
    <span class="clock">9:41</span>
    <svg class="back" viewBox="0 0 12 10"><path d="M11 5H2M5.5 1.5 2 5l3.5 3.5" fill="none" stroke="#0b0bef" stroke-width="1.3"/></svg>
    <div class="header">Jet Gallery</div>
    <div class="heading" style="top:73px;left:10px;line-height:17px">Meridian Grand Express<br>XR</div>
    <div class="photo" role="img" aria-label="Front view of the jet on the runway at twilight" style="top:115px;left:10px;width:103px;height:137px;background:linear-gradient(#2a3a7a,#6d7fb4 55%,#3a3e4e)"></div>
    <div class="photo" role="img" aria-label="Cockpit instrument panel" style="top:115px;left:120px;width:103px;height:137px;background:linear-gradient(#1a1c24,#3f4a62 50%,#22242c)"></div>
    <div class="photo" role="img" aria-label="Galley with polished wood cabinetry" style="top:259px;left:10px;width:103px;height:137px;background:linear-gradient(135deg,#5a3218,#b06a34 50%,#d9c0a0)"></div>
    <div class="photo" role="img" aria-label="Cabin lounge with leather seats and table" style="top:259px;left:120px;width:103px;height:137px;background:linear-gradient(135deg,#8a5a30,#c9a880 50%,#ece6de)"></div>
    <div class="photo" role="img" aria-label="Cabin seating area with a screen" style="top:404px;left:10px;width:103px;height:110px;background:linear-gradient(135deg,#7a4a24,#c9a07a 50%,#f0ece6)"></div>
  </section>
  <div class="caption" style="left:872px;top:640px">Jet Gallery</div>

  <!-- Flight details -->
  <section class="screen" style="left:94px;top:819px">
    <span class="clock">9:41</span>
    <svg class="back" viewBox="0 0 12 10"><path d="M11 5H2M5.5 1.5 2 5l3.5 3.5" fill="none" stroke="#0b0bef" stroke-width="1.3"/></svg>
    <div class="header">Flight Details</div>
    <div class="card" style="top:62px;left:10px;width:213px;height:192px;overflow:hidden">
      <div role="img" aria-label="World map showing the Pacific route" style="position:absolute;inset:10px 0 20px 0;background:radial-gradient(ellipse at 30% 60%,var(--map),rgba(220,220,251,.3) 70%),radial-gradient(ellipse at 85% 30%,var(--map),transparent 60%)"></div>
      <svg style="position:absolute;left:0;top:0" width="213" height="192" viewBox="0 0 213 192"><path d="M46 157 Q110 64 200 53" fill="none" stroke="#0b0bef" stroke-width="1"/><circle cx="200" cy="53" r="2.5" fill="#fff" stroke="#0b0bef"/><circle cx="46" cy="157" r="2" fill="#0b0bef"/><text x="190" y="45" font-family="Jost,sans-serif" font-size="10" font-weight="600" fill="#0b0bef">JFK</text><text x="36" y="173" font-family="Jost,sans-serif" font-size="10" font-weight="600" fill="#0b0bef">SYD</text></svg>
    </div>
    <div class="card" style="top:271px;left:10px;width:213px;height:56px">
      <div class="label" style="position:absolute;left:32px;top:10px">Departure</div>
      <div class="value" style="position:absolute;left:15px;top:27px">New York - JFK</div>
      <div class="label" style="position:absolute;left:146px;top:10px">Arrival</div>
      <div class="value" style="position:absolute;left:123px;top:27px">Sydney - SYD</div>
      <div class="round-btn" style="position:absolute;left:96px;top:17px;width:20px;height:20px"><svg width="10" height="10" viewBox="0 0 10 10"><path d="M1.5 3.5h7M6.8 1.8 8.5 3.5 6.8 5.2M8.5 6.5h-7M3.2 4.8 1.5 6.5 3.2 8.2" fill="none" stroke="#fff" stroke-width="1"/></svg></div>
    </div>
    <div class="card" style="top:342px;left:10px;width:213px;height:80px"></div>
    <div class="row" style="top:349px;left:18px;right:18px"><span>Via</span><b style="font-size:7px;color:var(--soft)">Direct</b></div>
    <div class="row" style="top:375px;left:18px;right:18px"><span>Distance</span><b>7,419 mi</b></div>
    <div class="row" style="top:401px;left:18px;right:18px"><span>Est. Flight Time</span><b>14 hours 35 minutes</b></div>
    <div class="round-btn" style="top:466px;left:10px"><svg width="12" height="12" viewBox="0 0 12 12"><circle cx="6" cy="6" r="3.6" fill="none" stroke="#fff" stroke-width="2.2" stroke-dasharray="1.6 1.2"/><circle cx="6" cy="6" r="1.4" fill="#fff"/></svg></div>
    <div class="round-btn" style="top:466px;left:196px"><svg width="12" height="12" viewBox="0 0 12 12"><circle cx="9" cy="2.5" r="1.7" fill="#fff"/><circle cx="3" cy="6" r="1.7" fill="#fff"/><circle cx="9" cy="9.5" r="1.7" fill="#fff"/><path d="M9 2.5 3 6l6 3.5" fill="none" stroke="#fff" stroke-width="1"/></svg></div>
  </section>
  <div class="caption" style="left:94px;top:1361px">Flight Details</div>

  <!-- Settings popup -->
  <section class="screen" style="left:483px;top:819px">
    <div class="faded" style="inset:0">
      <div class="header">Flight Details</div>
      <div class="card" style="position:absolute;top:62px;left:10px;width:213px;height:192px;background:var(--map)"></div>
      <div class="card" style="position:absolute;top:342px;left:10px;width:213px;height:80px;background:var(--soft)"></div>
    </div>
    <div class="card" style="top:181px;left:10px;width:213px;height:135px"></div>
    <div class="heading" style="top:189px;left:18px">Settings</div>
    <div class="row" style="top:222px;left:18px;right:12px;font-size:10px"><span>Units</span><span style="color:var(--blue)">Miles - Mi &nbsp;⇕</span></div>
    <div class="row" style="top:254px;left:18px;right:14px;font-size:10px"><span>Developers Contact</span><span style="color:var(--blue)">›</span></div>
    <div class="row" style="top:285px;left:18px;right:14px;font-size:10px"><span>Rate and Review</span><span style="color:var(--blue)">›</span></div>
  </section>
  <div class="caption" style="left:483px;top:1361px">Settings Popup</div>

  <!-- Share -->
  <section class="screen" style="left:872px;top:819px">
    <span class="clock">9:41</span>
    <svg class="back" viewBox="0 0 12 10"><path d="M11 5H2M5.5 1.5 2 5l3.5 3.5" fill="none" stroke="#0b0bef" stroke-width="1.3"/></svg>
    <div class="header">Flight Details</div>
    <div class="card" style="top:62px;left:10px;width:213px;height:192px;overflow:hidden">
      <div role="img" aria-label="World map showing the Pacific route" style="position:absolute;inset:10px 0 20px 0;background:radial-gradient(ellipse at 30% 60%,var(--map),rgba(220,220,251,.3) 70%),radial-gradient(ellipse at 85% 30%,var(--map),transparent 60%)"></div>
      <svg style="position:absolute;left:0;top:0" width="213" height="192" viewBox="0 0 213 192"><path d="M46 157 Q110 64 200 53" fill="none" stroke="#0b0bef" stroke-width="1"/><circle cx="200" cy="53" r="2.5" fill="#fff" stroke="#0b0bef"/><circle cx="46" cy="157" r="2" fill="#0b0bef"/><text x="190" y="45" font-family="Jost,sans-serif" font-size="10" font-weight="600" fill="#0b0bef">JFK</text><text x="36" y="173" font-family="Jost,sans-serif" font-size="10" font-weight="600" fill="#0b0bef">SYD</text></svg>
    </div>
    <div class="card" style="top:271px;left:10px;width:213px;height:56px">
      <div class="label" style="position:absolute;left:32px;top:10px">Departure</div>
      <div class="value" style="position:absolute;left:15px;top:27px">New York - JFK</div>
      <div class="label" style="position:absolute;left:146px;top:10px">Arrival</div>
      <div class="value" style="position:absolute;left:123px;top:27px">Sydney - SYD</div>
      <div class="round-btn" style="position:absolute;left:96px;top:17px;width:20px;height:20px"><svg width="10" height="10" viewBox="0 0 10 10"><path d="M1.5 3.5h7M6.8 1.8 8.5 3.5 6.8 5.2M8.5 6.5h-7M3.2 4.8 1.5 6.5 3.2 8.2" fill="none" stroke="#fff" stroke-width="1"/></svg></div>
    </div>
    <div class="card" style="top:342px;left:10px;width:213px;height:80px"></div>
    <div class="row" style="top:349px;left:18px;right:18px"><span>Via</span><b style="font-size:7px;color:var(--soft)">Direct</b></div>
    <div class="sheet" style="top:378px;left:0;width:233px;height:131px">
      <div class="heading" style="position:absolute;left:10px;top:10px">Choose an app</div>
      <div style="position:absolute;right:10px;top:5px;font-size:12px;color:var(--blue)">×</div>
      <div class="app" style="position:absolute;left:12px;top:47px"><i style="border-color:#2bbf5a"></i>Chatter</div>
      <div class="app" style="position:absolute;left:83px;top:47px"><i style="border-color:#e04434"></i>Mailer</div>
      <div class="app" style="position:absolute;left:155px;top:47px"><i style="border-color:#1e7bf2"></i>Pinger</div>
      <div style="position:absolute;left:0;width:100%;top:91px;text-align:center;font-size:6px;color:var(--mid)">View all<br><span style="color:var(--blue);font-size:8px">⌄</span></div>
    </div>
  </section>
  <div class="caption" style="left:872px;top:1361px">Share Flight Details</div>

  <!-- Developers contact -->
  <section class="screen" style="left:483px;top:1539px">
    <span class="clock">9:41</span>
    <svg class="back" viewBox="0 0 12 10"><path d="M11 5H2M5.5 1.5 2 5l3.5 3.5" fill="none" stroke="#0b0bef" stroke-width="1.3"/></svg>
    <div class="header">Developers Contact</div>
    <div class="wordmark" style="top:130px;font-size:17px;letter-spacing:.28em">SKYVELOUR</div>
    <div class="contact-title" style="top:210px">Developed By:</div>
    <div class="contact-text" style="top:236px">SkyVelour Ltd</div>
    <div class="contact-title" style="top:274px">Email:</div>
    <div class="contact-text" style="top:300px">customersupport@skyvelour.example</div>
    <div class="contact-title" style="top:338px">Head Office:</div>
    <div class="contact-text" style="top:364px;line-height:15px">48 Harbor Lane, Westfield,<br>TX 75012</div>
    <div class="contact-title" style="top:418px">Social Links:</div>
    <div class="social" style="top:443px;left:58px;background:#3b5a9a"></div>
    <div class="social" style="top:443px;left:100px;background:#2ea4ee"></div>
    <div class="social" style="top:443px;left:142px;background:#ee2f5a"></div>
  </section>
  <div class="caption" style="left:483px;top:2082px">Developers Contact</div>

</div>
</body>
</html>
```